KJ Glimmer Cleaning Business Card

We need a business card for our new business, a cleaning company using steam. We already have a logo, and would like a modern-looking card using colors that go well with those in our logo.

```html
<!DOCTYPE html>
<html lang="en">
<head>
<meta charset="utf-8">
<title>KJ Glimmer Cleaning Business Card</title>
<link href="https://fonts.googleapis.com/css2?family=Open+Sans:wght@400;600;700&display=swap" rel="stylesheet">
<style>
  :root {
    --page: #e9e9e6;
    --ink-black: #0c0d10;
    --steam-blue: #5aa6e6;
    --deep-blue: #2f78cf;
    --lime: #9fd23a;
    --text-dark: #1d2330;
    --white: #ffffff;
  }
  * { box-sizing: border-box; margin: 0; padding: 0; }
  html, body { width: 1200px; height: 1023px; overflow: hidden; }
  body {
    background: var(--page);
    font-family: "Open Sans", Arial, sans-serif;
    position: relative;
  }
  .card {
    position: absolute;
    top: 361px;
    width: 525px;
    height: 300px;
    border-radius: 6px;
    overflow: hidden;
    box-shadow: 0 6px 18px rgba(0,0,0,0.18);
  }
  .card--front { left: 50px; background: var(--ink-black); }
  .card--back { left: 625px; }

  .card__art { position: absolute; inset: 0; width: 100%; height: 100%; }

  .brand {
    position: absolute;
    left: 34px;
    top: 42px;
    display: flex;
    align-items: center;
    gap: 12px;
  }
  .brand__dot {
    width: 28px; height: 28px; border-radius: 50%;
    background: var(--lime);
  }
  .brand__name {
    font-weight: 700;
    font-size: 22px;
    color: var(--steam-blue);
    letter-spacing: 0.2px;
    white-space: nowrap;
  }
  .person {
    position: absolute;
    left: 34px;
    top: 100px;
    display: flex;
    align-items: center;
    gap: 10px;
    white-space: nowrap;
  }
  .person__name { color: var(--steam-blue); font-size: 17px; font-weight: 600; letter-spacing: 0.5px; }
  .person__rule { width: 1px; height: 18px; background: var(--lime); }
  .person__title { color: var(--lime); font-size: 12px; font-weight: 600; letter-spacing: 0.5px; }

  .contact {
    position: absolute;
    left: 40px;
    top: 192px;
    list-style: none;
    font-size: 12.5px;
    color: var(--text-dark);
    white-space: nowrap;
  }
  .contact__item { display: flex; align-items: center; gap: 8px; height: 21px; }
  .contact__icon { width: 14px; height: 14px; flex: none; }
  .contact__item--address { margin-top: 5px; letter-spacing: 0.3px; }

  .back-name {
    position: absolute;
    left: 0; right: 0;
    top: 128px;
    text-align: center;
    font-weight: 700;
    font-size: 34px;
    color: var(--white);
  }
</style>
</head>
<body>

  <section class="card card--front" aria-label="Business card front">
    <svg class="card__art" viewBox="0 0 525 300" aria-hidden="true">
      <defs>
        <linearGradient id="waveBlue" x1="0" y1="0" x2="1" y2="1">
          <stop offset="0" stop-color="#9ccbf1"/>
          <stop offset="0.55" stop-color="#d6eaf8"/>
          <stop offset="1" stop-color="#b4d5f2"/>
        </linearGradient>
      </defs>
      <path d="M0 178 C220 178 360 150 395 0 L440 0 C420 120 360 220 320 300 L0 300 Z" fill="#4a90dc"/>
      <path d="M0 192 C230 192 372 160 409 0 L440 0 C420 120 360 220 320 300 L0 300 Z" fill="url(#waveBlue)"/>
    </svg>
    <svg class="card__art" viewBox="0 0 525 300" role="img" aria-label="Green dot pattern decoration">
      <defs>
        <linearGradient id="dotTone" x1="0" y1="0" x2="0" y2="1">
          <stop offset="0" stop-color="#b5dc4a"/>
          <stop offset="1" stop-color="#3f9a2a"/>
        </linearGradient>
      </defs>
      <path d="M458 0 L525 0 L525 300 L340 300 C378 220 438 120 458 0 Z" fill="url(#dotTone)"/>
    </svg>

    <div class="brand">
      <span class="brand__dot"></span>
      <span class="brand__name">KJ Glimmer Cleaning</span>
    </div>

    <div class="person">
      <span class="person__name">DANA MARLOW</span>
      <span class="person__rule"></span>
      <span class="person__title">DIRECTOR</span>
    </div>

    <ul class="contact">
      <li class="contact__item">
        <svg class="contact__icon" viewBox="0 0 14 14" aria-hidden="true"><circle cx="7" cy="7" r="7" fill="#9fd23a"/><path d="M4.5 3.5 L6 3.5 L6.6 5.4 L5.7 6.1 C6.2 7.2 6.9 7.9 8 8.4 L8.7 7.5 L10.5 8.1 L10.5 9.6 C7 9.8 4.3 7 4.5 3.5 Z" fill="#fff"/></svg>
        555.014.2290
      </li>
      <li class="contact__item">
        <svg class="contact__icon" viewBox="0 0 14 14" aria-hidden="true"><circle cx="7" cy="7" r="7" fill="#9fd23a"/><rect x="3.5" y="4.5" width="7" height="5" fill="none" stroke="#fff" stroke-width="1"/><path d="M3.5 4.5 L7 7.3 L10.5 4.5" fill="none" stroke="#fff" stroke-width="1"/></svg>
        DMarlow@KJglimmercleaning.com
      </li>
      <li class="contact__item">
        <svg class="contact__icon" viewBox="0 0 14 14" aria-hidden="true"><circle cx="7" cy="7" r="7" fill="#9fd23a"/><circle cx="7" cy="7" r="3.6" fill="none" stroke="#fff" stroke-width="0.9"/><path d="M3.4 7 H10.6 M7 3.4 C5.4 5.5 5.4 8.5 7 10.6 M7 3.4 C8.6 5.5 8.6 8.5 7 10.6" fill="none" stroke="#fff" stroke-width="0.8"/></svg>
        www.KJglimmercleaning.com
      </li>
      <li class="contact__item contact__item--address">P.O. BOX 4172 FAIRVIEW, MS 39021</li>
    </ul>
  </section>

  <section class="card card--back" aria-label="Business card back">
    <svg class="card__art" viewBox="0 0 525 300" role="img" aria-label="Soft blue dot pattern with light streaks">
      <defs>
        <linearGradient id="backTone" x1="0" y1="0" x2="1" y2="1">
          <stop offset="0" stop-color="#4f95dc"/>
          <stop offset="0.5" stop-color="#6fb3ea"/>
          <stop offset="1" stop-color="#2f78cf"/>
        </linearGradient>
      </defs>
      <rect width="525" height="300" fill="url(#backTone)"/>
    </svg>
    <div class="back-name">KJ Glimmer Cleaning</div>
  </section>

</body>
</html>
```